Bakery Replacement Lighted Sign Face

We are opening a new bakery that sells only cakes. The name is "The Willow Lantern." We are replacing the current sign face with a new look that states our name and makes a bold statement of fun. We will be known for having 101 cakes that are always ready for immediate pickup or delivery. Our colors are pink, orange, and lime green. An image is provided to see the colors.

Target Market(s)

people who buy cakes for parties and all other occasions

Industry/Entity Type

Cakes

Other font styles liked:
• look at the logo and file for the main font name

Colors
59FF00
82FF00
B8FF75
E3FFCB
F4FFEA
F0912C
F2A743
F7CA91
FBE8D2
FDF5EE
EB3D1F
EC4F4E
F09395
F8D3D4
FCEDEE

Requirements
Must have
• The name of the bakery. Logo can be used as is or changed as shown in one of the uploaded PDFs. Must use either pink, orange, lime green, white, or black. We prefer a bright pink background with white lettering as our first choice, but are willing to be open minded to see all creative concepts. Also the sign is 14 feet long and 42 inches tall so the artwork must fit within those boundaries. Also keep in mind the sign does have a 4 inch black frame. So the graphics area is actually 13 feet 2 inches by 3 feet. Also, in the attached pdf that shows a rough possible layout, the words "101 cakes to go" is on the sign. It is NOT a must. Only use the wording if it adds to your design.
Nice to have
• You are welcome to add additional stars or other fun graphics that could look good.
Should not have
• No images of cakes or other bakery products.

```html
<!DOCTYPE html>
<html lang="en">
<head>
<meta charset="utf-8">
<title>The Willow Lantern – 101 Cakes To Go</title>
<link rel="stylesheet" href="https://fonts.googleapis.com/css2?family=Fredoka:wght@600&display=swap">
<style>
  :root {
    --orange: #F0912C;
    --orange-soft: #F2A743;
    --orange-pale: #F7CA91;
    --pink: #EC4F4E;
    --pink-bright: #EB3D1F;
    --pink-soft: #F09395;
    --lime: #82FF00;
    --white: #FFFFFF;
    --black: #1A1A1A;
  }
  html, body {
    margin: 0;
    padding: 0;
    overflow: hidden;
  }
  .sign-face {
    position: relative;
    width: 1200px;
    height: 273px;
    background: var(--orange);
    overflow: hidden;
    font-family: "Fredoka", sans-serif;
  }
  .backdrop {
    position: absolute;
    inset: 0;
  }
  .brand-name {
    position: absolute;
    left: 14px;
    top: 96px;
    width: 200px;
    margin: 0;
    text-align: center;
    color: var(--white);
    font-size: 36px;
    font-weight: 600;
    line-height: 40px;
  }
  .headline {
    position: absolute;
    left: 383px;
    top: 38px;
    width: 600px;
    margin: 0;
    text-align: center;
    color: var(--white);
    font-size: 80px;
    font-weight: 600;
    line-height: 72px;
    letter-spacing: 1px;
  }
</style>
</head>
<body>
<main class="sign-face">
  <svg class="backdrop" width="1200" height="273" viewBox="0 0 1200 273" xmlns="http://www.w3.org/2000/svg">
    <ellipse role="img" aria-label="Illustrated pastry" cx="282" cy="112" rx="40" ry="60" fill="var(--orange-soft)"/>
    <circle class="brand-disc" cx="28" cy="135" r="237" fill="var(--pink)"/>
    <rect role="img" aria-label="Illustrated cupcake" x="332" y="-10" width="104" height="44" rx="14" fill="var(--pink-soft)"/>
    <circle role="img" aria-label="Illustrated cake ball" cx="396" cy="114" r="42" fill="var(--orange-pale)"/>
    <ellipse role="img" aria-label="Illustrated leaf" cx="447" cy="188" rx="13" ry="27" transform="rotate(30 447 188)" fill="var(--lime)"/>
    <ellipse role="img" aria-label="Illustrated éclair" cx="300" cy="250" rx="108" ry="38" transform="rotate(-8 300 250)" fill="var(--black)"/>
    <ellipse role="img" aria-label="Illustrated pretzel" cx="559" cy="262" rx="78" ry="58" fill="var(--orange-soft)"/>
    <ellipse role="img" aria-label="Illustrated macaron" cx="792" cy="266" rx="52" ry="42" fill="var(--pink-soft)"/>
    <ellipse role="img" aria-label="Illustrated madeleine" cx="969" cy="72" rx="54" ry="70" transform="rotate(-15 969 72)" fill="var(--orange-soft)"/>
    <ellipse role="img" aria-label="Illustrated cookie" cx="1150" cy="48" rx="55" ry="52" fill="var(--orange-pale)"/>
    <ellipse role="img" aria-label="Illustrated croissant" cx="944" cy="220" rx="76" ry="56" transform="rotate(20 944 220)" fill="var(--orange-soft)"/>
    <ellipse role="img" aria-label="Illustrated frosted doughnut" cx="1130" cy="216" rx="82" ry="62" transform="rotate(15 1130 216)" fill="var(--black)"/>
  </svg>
  <p class="brand-name">The Willow<br>Lantern</p>
  <h1 class="headline">101 CAKES<br>TO GO</h1>
</main>
</body>
</html>
```